Design a calming beauty medical salon & spa website based in Hong Kong

We need help building an informational website for a beauty salon in Hong Kong. The local salon provides facials, massages, body and other slimming treatments in a relaxing environment. We offer some non-invasive medical treatments, such as botox. Having built the business on word of mouth, it is now time for us to launch a website to help market the business better. Website requirements:

-Must be responsive
-Use vibrant but clean colours. not too many, 1-2 colours
-Must be bilingual (switch between Chinese traditional and English)
-Our current website is host on a server, not using any particular platforms like wordpress

Pages:
1/ Homepage
2/ About us (incorporate gallery of salon photos and history of company)
3/ Promotions and latest deals (and leads them to sign up for more info, maybe pop-up small window when you click on a promotion)
4/ Treatment menus
4.1/Body treatments
4.2/ Face treatments
4.3/ Slimming treatments
5/ Showcasing products sold (no e-commerce functionality, just showing off products)
6/ Contact us (tel, address, map, opening hrs)

Footer - must haves include contact us info, privacy policy, terms & conditions, copyright blurb, join our company/employment page (with a form)

For information (comparable websites we like):
http://velarine.com/
http://mottaqua.com.hk/tc/aboutmottaqua/background.php#centerenvi
Attaching a very first draft concept for this website
Attaching pictures of the beauty salon
Attaching logo

Target Market(s)

Hong Kong based, Chinese, females, 30-50+ age. 90% female clients.

Industry/Entity Type

Beauty Salon

Number of Pages Required

5+ page

Font styles to use
Sans Serif

Colors
f9d9e8
fbd3d4
fee3d5
fbe7d2
fee18a
fbf289
ffffff

Requirements
Must have
• interactive elements on website, such as scrolling banner photo headers
• incorporate photos of website salon
• connect to facebook page

```html
<!DOCTYPE html>
<html lang="zh-Hant">
<head>
<meta charset="utf-8">
<title>Lumena Beauty 瑩光醫學美容</title>
<link rel="stylesheet" href="https://fonts.googleapis.com/css2?family=Noto+Sans+TC:wght@300;400;500&display=swap">
<style>
:root{
  --purple:#6b1d8c;
  --pink:#fbd3d4;
  --pink-soft:#f9d9e8;
  --yellow:#fde2a0;
  --text:#4a4a4a;
  --muted:#666;
  --white:#ffffff;
}
*{margin:0;padding:0;box-sizing:border-box}
html,body{width:1200px;height:2568px;overflow:hidden;background:var(--white)}
body{position:relative;font-family:"Noto Sans TC",sans-serif;color:var(--text);font-weight:300}
.abs{position:absolute}
/* header */
.site-header{position:absolute;left:0;top:0;width:1200px;height:96px;background:var(--white);z-index:5}
.brand{position:absolute;left:135px;top:30px;display:flex;align-items:center;gap:10px;color:var(--purple);font-size:24px;font-weight:500}
.brand-dot{width:26px;height:26px;border-radius:50%;background:var(--purple)}
.contact-mini{position:absolute;left:760px;top:16px;display:flex;align-items:center;gap:10px;font-size:10px;line-height:13px;color:var(--text)}
.icon-dot{width:18px;height:18px;border-radius:50%;background:var(--purple)}
.sep{width:1px;height:16px;background:#999}
.lang{position:absolute;left:990px;top:20px;font-size:14px;font-weight:400}
.lang .cn{color:var(--purple)}
.main-nav{position:absolute;left:614px;top:58px;display:flex;gap:33px;font-size:15px;font-weight:400;color:#333}
/* hero */
.hero{position:absolute;left:0;top:96px;width:1200px;height:500px}
.hero-photo{position:absolute;left:0;top:0;width:370px;height:490px;background:radial-gradient(ellipse at 40% 45%,#f6ddd0 0%,#eed0c4 45%,#f4e6e2 100%)}
.hero-brand{position:absolute;left:520px;top:130px;width:480px;text-align:center;color:var(--purple)}
.hero-brand .en{font-size:62px;font-weight:500;line-height:1}
.hero-brand .zh{font-size:44px;font-weight:400;margin-top:38px;letter-spacing:2px;padding-left:90px}
/* services */
.section-title{position:absolute;left:0;width:1200px;text-align:center;font-size:38px;font-weight:300;color:#222}
.divider{position:absolute;left:512px;width:176px;height:20px}
.intro{position:absolute;left:0;top:775px;width:1200px;text-align:center;font-size:17px;line-height:25px;color:var(--muted)}
.service{position:absolute;top:978px;width:298px}
.service-photo{width:298px;height:185px;border-radius:6px}
.service-name{margin-top:16px;text-align:center;font-size:16px;color:var(--muted)}
/* contact */
.contact{position:absolute;left:0;top:1320px;width:1200px;height:542px}
.contact-body{position:absolute;left:0;top:1510px;width:1200px;text-align:center;font-size:18px;line-height:26px;color:#333}
.contact-body p{margin-bottom:26px}
.contact-body strong{font-weight:500}
.map{position:absolute;left:0;top:1862px;width:1200px;height:325px;background:linear-gradient(135deg,#f3f1ee 0%,#ece9e4 50%,#f5efe6 100%)}
/* footer */
.site-footer{position:absolute;left:0;top:2187px;width:1200px;height:381px;text-align:center}
.footer-brand{position:absolute;left:0;top:70px;width:1200px;display:flex;justify-content:center;align-items:center;gap:12px;color:var(--purple);font-size:32px;font-weight:500}
.footer-brand .brand-dot{width:36px;height:36px}
.social-dot{position:absolute;left:578px;top:182px;width:44px;height:44px;border-radius:50%;background:var(--purple)}
.footer-links{position:absolute;left:0;top:248px;width:1200px;font-size:17px;line-height:28px;color:#333}
.copyright{position:absolute;left:0;top:314px;width:1200px;font-size:17px;color:#333}
</style>
</head>
<body>

<header class="site-header">
  <div class="brand"><span class="brand-dot"></span>Lumena Beauty</div>
  <div class="contact-mini">
    <span class="icon-dot"></span><span class="sep"></span><span class="icon-dot"></span>
    <span>Tel:23456780<br>Whatsapp:61234567</span>
  </div>
  <div class="lang">ENG &nbsp;|&nbsp; <span class="cn">CN</span></div>
  <nav class="main-nav"><span>關於我們</span><span>迎新優惠</span><span>療程介紹</span><span>產品品牌</span><span>聯絡我們</span></nav>
</header>

<section class="hero">
  <svg class="abs" style="left:0;top:0" width="1200" height="500" viewBox="0 0 1200 500">
    <rect width="1200" height="500" fill="var(--pink)"/>
    <polygon points="620,0 1200,0 1200,0 860,500 300,500" fill="var(--yellow)"/>
  </svg>
  <div class="hero-photo" role="img" aria-label="Portrait of a woman with smooth skin touching her cheek"></div>
  <div class="hero-brand">
    <div class="en">Lumena Beauty</div>
    <div class="zh">瑩光醫學美容</div>
  </div>
  <svg class="abs" style="left:0;top:430px" width="1200" height="70" viewBox="0 0 1200 70">
    <path d="M0,70 L0,40 C300,-10 600,50 900,38 C1020,34 1120,50 1200,60 L1200,70 Z" fill="var(--white)"/>
  </svg>
</section>

<h2 class="section-title" style="top:676px">全方為美容服務</h2>
<svg class="divider" style="top:738px" viewBox="0 0 176 20">
  <line x1="0" y1="10" x2="66" y2="10" stroke="#555" stroke-width="1"/>
  <line x1="110" y1="10" x2="176" y2="10" stroke="#555" stroke-width="1"/>
  <circle cx="82" cy="10" r="6" fill="none" stroke="#555" stroke-width="1.3"/>
  <circle cx="94" cy="10" r="6" fill="none" stroke="#555" stroke-width="1.3"/>
</svg>
<p class="intro">以全方位角度照顧肌膚不同所需，提供面部及身體護理，<br>顧客可於休閒舒適的環境下盡情享受高效美肌療程。<br>配以尊貴瑞士品牌 Lumena Beauty有機素材系列作家居護理，<br>務求將肌膚質素推至巔峰。</p>

<div class="service" style="left:135px">
  <div class="service-photo" role="img" aria-label="Facial treatment photo" style="background:linear-gradient(135deg,#f7e3d8,#e9d6cc 60%,#f1e4dc)"></div>
  <div class="service-name">面部護理</div>
</div>
<div class="service" style="left:451px">
  <div class="service-photo" role="img" aria-label="Body treatment photo" style="background:linear-gradient(135deg,#eeeae6,#e3dcd6 60%,#f1eeeb)"></div>
  <div class="service-name">身體護理</div>
</div>
<div class="service" style="left:767px">
  <div class="service-photo" role="img" aria-label="Slimming massage photo" style="background:linear-gradient(135deg,#e9d9cc,#d8c0ad 55%,#efe4dc)"></div>
  <div class="service-name">纖形瘦身</div>
</div>

<section class="contact">
  <svg class="abs" style="left:0;top:0" width="1200" height="542" viewBox="0 0 1200 542">
    <rect width="1200" height="542" fill="var(--pink)"/>
    <polygon points="490,0 1090,0 720,542 150,542" fill="var(--yellow)"/>
    <path d="M0,0 L1200,0 L1200,20 C1000,-2 800,30 600,22 C400,14 200,40 0,26 Z" fill="var(--white)"/>
  </svg>
</section>
<h2 class="section-title" style="top:1410px">聯絡我們</h2>
<svg class="divider" style="top:1472px" viewBox="0 0 176 20">
  <line x1="0" y1="10" x2="66" y2="10" stroke="#555" stroke-width="1"/>
  <line x1="110" y1="10" x2="176" y2="10" stroke="#555" stroke-width="1"/>
  <circle cx="82" cy="10" r="6" fill="none" stroke="#555" stroke-width="1.3"/>
  <circle cx="94" cy="10" r="6" fill="none" stroke="#555" stroke-width="1.3"/>
</svg>
<div class="contact-body">
  <p>星期一至五：早上10:30至 晚上9:30<br>星期六及假期：早上10:30至 晚上7:30</p>
  <p><strong>查詢熱線：</strong><br>23456780 ｜ 61234567</p>
  <p>加蓮道12號瑩光大廈8樓全層<br>九龍尖沙咀</p>
  <p>hello@lumenabeauty.hk</p>
</div>

<div class="map" role="img" aria-label="Street map showing the salon location in Tsim Sha Tsui"></div>

<footer class="site-footer">
  <div class="footer-brand"><span class="brand-dot"></span>Lumena Beauty</div>
  <div class="social-dot"></div>
  <div class="footer-links">條款及細則<br>加入我們</div>
  <div class="copyright">Copyright©2017 Lumena Beauty HK Ltd. All rights reserved.</div>
</footer>

</body>
</html>
```